A punchy one page sell-shell for a new product for surfers: the Tide-Tine Board Tether

The Tide Tine Board Tether is a product for surfers. Most surfers use a leash (also called "leg rope") to keep the board attached to one leg. Surfers also use wax spread on their boards to create grip and avoid slipping when stepping on the soaked board.
A wax comb is used to scratch old wax and return the grip to its surface.
I recently patented a product design that includes the wax comb in the leash so that it is always available.
This project is to create a one pager sell sheet about this product. The sell sheet aims to grab attention of product developers of surfing brands that might want to manufacture this product under license.

Target Market(s)

The sell sheet must appeal to, and will be sent to, Product Developers, Product Designers, and Industrial Designers that work for the surfing hardware industry. Examples of companies in this industry: RBV, Brevik Coastal Gearworks, MORVALE, Pelican Drift Supply, Kelp Vista, QJ, Harbor and Pine, amongst others...
On the other hand, the target market for the product are all surfers around the world.
Note: many, probably most, Product Developers in the surfing industry are also surfers.

Industry/Entity Type

Product

Font styles to use
Sans Serif
Other font styles liked:
• anything goes

Requirements
Must have
• Some surfing related images: a surfer, a wave.
• Text explaining the product and benefits. Refer to examples of previous sell sheets.
Nice to have
• An image of a surfer surfing where the leash (leg rope) is seen.
Should not have
• Other brands, company names
• Photos of professional athletes where this can be identified

```html
<!DOCTYPE html>
<html lang="en">
<head>
<meta charset="utf-8">
<title>The Tide Tine Board Tether – Sell Sheet</title>
<link rel="stylesheet" href="https://fonts.googleapis.com/css2?family=Fira+Sans+Extra+Condensed:wght@400;500;600&display=swap">
<style>
  :root {
    --stage: #3a3836;
    --cream-top: #fdf6e0;
    --cream-bottom: #fbe6b4;
    --title-band: #bde0e6;
    --accent-blue: #2ea5d9;
    --ink: #111111;
    --rule: #222222;
    --sky: #ece7d6;
    --sea: #8fa1a8;
    --sand: #d9c7a8;
    --inset-fill: #dcdde3;
  }
  * { margin: 0; padding: 0; box-sizing: border-box; }
  html, body {
    width: 900px; height: 1200px; overflow: hidden;
    background: var(--stage);
  }
  .canvas {
    position: relative; width: 900px; height: 1200px;
    display: flex; justify-content: center; align-items: center;
  }
  .sheet {
    position: relative;
    width: 685px; height: 970px;
    transform: scale(1.237);
    flex-shrink: 0;
    background: linear-gradient(180deg, var(--cream-top) 30%, var(--cream-bottom) 100%);
    font-family: "Fira Sans Extra Condensed", "Arial Narrow", sans-serif;
    color: var(--ink);
    overflow: hidden;
  }
  .hero { position: absolute; left: 0; top: 0; width: 685px; height: 360px; }
  .title-band {
    position: absolute; left: 0; top: 373px; width: 685px; height: 60px;
    background: var(--title-band);
    display: flex; align-items: center; justify-content: center;
  }
  .title-band h1 { font-size: 44px; font-weight: 600; letter-spacing: 0.3px; }
  .intro {
    position: absolute; left: 104px; top: 447px;
    font-size: 19px; font-weight: 600; line-height: 28px;
  }
  .grid-rule-v { position: absolute; left: 357px; top: 530px; width: 1px; height: 226px; background: var(--rule); }
  .grid-rule-h { position: absolute; left: 0; top: 639px; width: 685px; height: 1px; background: var(--rule); }
  .feature { position: absolute; }
  .feature h2 { font-size: 34px; font-weight: 400; text-align: center; margin-bottom: 10px; }
  .feature p { font-size: 21px; line-height: 29px; }
  .feature-comb { left: 32px; top: 516px; width: 300px; }
  .feature-comb h2 { text-align: left; padding-left: 95px; }
  .feature-pain { left: 390px; top: 514px; width: 280px; }
  .feature-pain h2 { text-align: left; padding-left: 66px; }
  .feature-accessorize { left: 30px; top: 644px; width: 320px; }
  .feature-accessorize h2 { text-align: left; padding-left: 70px; }
  .feature-solution { left: 397px; top: 648px; width: 280px; }
  .feature-solution h2 { text-align: left; padding-left: 52px; }
  .call-now { position: absolute; left: 376px; top: 776px; }
  .call-now strong { display: block; font-size: 29px; font-weight: 400; line-height: 32px; }
  .call-now span { font-size: 23px; line-height: 28px; }
  .promo-band {
    position: absolute; left: 0; top: 847px; width: 685px; height: 73px;
    background: var(--accent-blue);
    text-align: center; font-size: 22px; line-height: 29px; padding-top: 8px;
  }
  .website { position: absolute; right: 21px; top: 926px; font-size: 21px; }
</style>
</head>
<body>
<div class="canvas">
  <article class="sheet">
    <svg class="hero" viewBox="0 0 685 360" width="685" height="360">
      <defs>
        <linearGradient id="beach" x1="0" y1="0" x2="0" y2="1">
          <stop offset="0" stop-color="var(--sky)"/>
          <stop offset="0.28" stop-color="var(--sky)"/>
          <stop offset="0.34" stop-color="var(--sea)"/>
          <stop offset="0.52" stop-color="#b9c0bc"/>
          <stop offset="0.62" stop-color="var(--sand)"/>
          <stop offset="1" stop-color="#e6d8bd"/>
        </linearGradient>
      </defs>
      <path role="img" aria-label="Photo: surfer walking into the sea carrying a board, leash strapped to the ankle"
            fill="url(#beach)"
            d="M0,0 H685 V90 C660,220 560,300 430,300 C360,300 330,280 260,300 C190,320 120,305 60,318 C35,323 15,320 0,318 Z"/>
      <path fill="none" stroke="var(--accent-blue)" stroke-width="4"
            d="M0,318 C15,320 35,323 60,318 C120,305 190,320 260,300 C330,280 360,300 430,300 C560,300 660,220 685,90"/>
      <circle role="img" aria-label="Illustration: leash ankle strap with built-in wax comb"
              cx="437" cy="285" r="60" fill="var(--inset-fill)" stroke="var(--accent-blue)" stroke-width="3"/>
      <circle role="img" aria-label="Illustration: wax comb in the strap scraping a board deck"
              cx="567" cy="222" r="95" fill="var(--inset-fill)" stroke="var(--accent-blue)" stroke-width="3"/>
    </svg>

    <header class="title-band"><h1>The Tide Tine Board Tether</h1></header>

    <p class="intro">Did you slip and miss the best wave of the day?<br>Never again with an integrated wax comb in your leash strap!</p>

    <div class="grid-rule-v"></div>
    <div class="grid-rule-h"></div>

    <section class="feature feature-comb">
      <h2>Comb</h2>
      <p>Easy to access comb allows you to get the traction you need to stay upright</p>
    </section>
    <section class="feature feature-pain">
      <h2>Pain</h2>
      <p>Sudfers need to scratch wax And often don't have with what</p>
    </section>
    <section class="feature feature-accessorize">
      <h2>Accessorize</h2>
      <p>Combs, Edges and Straps come in different colours so you can match easily</p>
    </section>
    <section class="feature feature-solution">
      <h2>Solution</h2>
      <p>New leash design in corporates wax comb in the strap</p>
    </section>

    <div class="call-now">
      <strong>Call Now</strong>
      <span>For More Information: 0198-765-432</span>
    </div>

    <footer class="promo-band">Leash strap Incorporates a Wax Comb that is always available.<br>Even when you are in the outside!</footer>
    <p class="website">www.tidetinegear.com.au</p>
  </article>
</div>
</body>
</html>
```